Harbor Lanterns: Walking Beside Young Ones Through Every Season

This book is about being a good father and how to parent them well so they are fully equipped to launch into the world when they become adults. It is an encouraging and practical guide that acknowledges the difficulties of being a good father and provides strategies for addressing them.

Target Market(s)

My target market is dads, or people that will gift this book to a dad that they know

```html
<!DOCTYPE html>
<html lang="en">
<head>
<meta charset="UTF-8">
<title>Harbor Lanterns — Book Cover</title>
<link rel="stylesheet" href="https://fonts.googleapis.com/css2?family=Bebas+Neue&family=Tinos:ital@1&display=swap">
<style>
  :root {
    --paper: #ffffff;
    --ink: #0a0a0a;
    --signal-red: #f80000;
    --art-cream: #f7dcae;
    --art-orange: #e9a24a;
    --art-rust: #b8552f;
    --art-teal: #5f8f86;
    --art-plum: #8c7388;
  }
  * { margin: 0; padding: 0; box-sizing: border-box; }
  html, body {
    width: 848px;
    height: 1200px;
    overflow: hidden;
    background: var(--paper);
  }
  .cover {
    position: relative;
    width: 848px;
    height: 1200px;
    background: var(--paper);
    color: var(--ink);
  }
  .title-lead {
    position: absolute;
    top: 58px;
    left: 0;
    width: 100%;
    text-align: center;
    font-family: "Bebas Neue", sans-serif;
    font-size: 94px;
    line-height: 1;
    letter-spacing: 0.16em;
    padding-left: 0.16em;
    color: var(--ink);
  }
  .title-main {
    position: absolute;
    top: 138px;
    left: 0;
    width: 100%;
    text-align: center;
    font-family: "Bebas Neue", sans-serif;
    font-size: 250px;
    line-height: 1;
    letter-spacing: 0.005em;
    color: var(--signal-red);
  }
  .rule {
    position: absolute;
    left: 138px;
    width: 592px;
    height: 4px;
    background: linear-gradient(90deg, rgba(248,0,0,0) 0%, var(--signal-red) 30%, var(--signal-red) 70%, rgba(248,0,0,0) 100%);
  }
  .rule--top { top: 365px; }
  .rule--bottom { top: 477px; }
  .subtitle {
    position: absolute;
    top: 382px;
    left: 0;
    width: 100%;
    text-align: center;
    font-family: "Tinos", serif;
    font-style: italic;
    text-transform: uppercase;
    font-size: 35px;
    line-height: 46px;
    letter-spacing: 0.1em;
    color: var(--ink);
  }
  .subtitle .accent { color: var(--signal-red); }
  .cover-art {
    position: absolute;
    top: 530px;
    left: 132px;
    width: 594px;
    height: 554px;
    border-radius: 40px 40px 10px 10px;
    background:
      radial-gradient(ellipse at 55% 30%, var(--art-cream) 0%, rgba(247,220,174,0) 45%),
      radial-gradient(ellipse at 35% 60%, rgba(184,85,47,0.55) 0%, rgba(184,85,47,0) 40%),
      linear-gradient(135deg, var(--art-plum) 0%, var(--art-orange) 40%, var(--art-cream) 60%, var(--art-teal) 100%);
    opacity: 0.9;
  }
  .author {
    position: absolute;
    top: 1120px;
    left: 0;
    width: 100%;
    text-align: center;
    font-family: "Bebas Neue", sans-serif;
    font-size: 60px;
    line-height: 1;
    letter-spacing: 0.1em;
    padding-left: 0.1em;
    color: var(--ink);
  }
</style>
</head>
<body>
  <main class="cover">
    <h1>
      <span class="title-lead">Harbor</span>
      <span class="title-main">Lanterns</span>
    </h1>
    <div class="rule rule--top"></div>
    <p class="subtitle">Walking Beside <span class="accent">Young Ones</span><br>Through Every Season</p>
    <div class="rule rule--bottom"></div>
    <div class="cover-art" role="img" aria-label="Watercolour illustration of a bearded father in a plaid shirt hugging his two young children, with small hearts around them"></div>
    <p class="author">Author Name</p>
  </main>
</body>
</html>
```